The Lantern Harbor Summit (Poster or Color Flyer)

Unique and not too traditional design with Wording:
The Lantern Harbor Summit: The Deeper Message of God's Relentless Love
Friday Aug. 5 - Sunday the 7th
Denver 2016
www.TheLanternSummit.example
Updates
Project Deadline Extended
Reason: Our first experience with this type of design service was with 47Pixel, and we received 140 designs within a week.
We received only 2 designers submissions by our first 5 days with Mosaic Bench. We received an email that our time would be extended, which is much appreciated. The last 24 hours has brought in several new designs - which is great. However, we have a team of reviewers on our end - and due to Christmas break, will not be able to make a decision until January 4 or 5.
Can our deadline be moved to January 5? (at no charge?)
THANKS,
Trevor
Target Market(s)
General public. Professors. Pastors.
Requirements
Must have
- Basic info above.
Nice to have
- Subtle verses tucked into the graphics
- See www.TheQKTs.example for some of these,
- such as Romans 11:32, 1 John 2:2, 1 Timothy 4:10, John 12:32
Should not have
- Typical religious appearance.

```html
<!DOCTYPE html>
<html lang="en">
<head>
<meta charset="utf-8">
<title>The QKTs – The Lantern Harbor Summit</title>
<link rel="stylesheet" href="https://fonts.googleapis.com/css2?family=Arvo:wght@700&family=Libre+Baskerville:wght@400;700&family=Tinos:wght@700&display=swap">
<style>
  :root {
    --navy: #163a78;
    --sky-blue: #1f7fc6;
    --ink: #2a2016;
    --panel-fill: rgba(255, 255, 255, 0.72);
    --panel-edge: #9fd3f0;
    --white: #ffffff;
    --bg-top: #cfe9f8;
    --bg-mid: #4b93d3;
    --bg-low: #1d4fa0;
    --bg-deep: #0b1f5c;
    --crowd-dark: #0e2a6a;
    --crowd-glow: #3f8f6a;
    --city-red: #d9503f;
    --city-gold: #e2c25a;
  }
  * { margin: 0; padding: 0; box-sizing: border-box; }
  html, body { width: 928px; height: 1200px; overflow: hidden; }
  body { position: relative; background: var(--bg-deep); }

  .poster { position: relative; width: 928px; height: 1200px; overflow: hidden; }

  .artwork {
    position: absolute; inset: 0;
    background:
      radial-gradient(ellipse 18% 12% at 88% 52%, rgba(217,80,63,0.55), rgba(217,80,63,0) 70%),
      radial-gradient(ellipse 14% 10% at 8% 35%, rgba(226,194,90,0.45), rgba(226,194,90,0) 70%),
      radial-gradient(circle at 50% 42%, rgba(255,255,255,0.55) 0%, rgba(190,225,245,0.45) 30%, rgba(255,255,255,0) 48%),
      linear-gradient(180deg, var(--bg-top) 0%, #8ec5ec 22%, var(--bg-mid) 45%, #2f6fba 62%, var(--bg-low) 75%, var(--bg-deep) 100%);
  }
  .crowd {
    position: absolute; left: 0; right: 0; top: 640px; bottom: 0;
    background:
      radial-gradient(ellipse 22% 16% at 48% 30%, rgba(226,194,90,0.55), rgba(226,194,90,0) 70%),
      radial-gradient(ellipse 30% 22% at 45% 45%, rgba(63,143,106,0.6), rgba(63,143,106,0) 75%),
      radial-gradient(ellipse 20% 14% at 85% 20%, rgba(217,80,63,0.45), rgba(217,80,63,0) 70%),
      linear-gradient(180deg, rgba(14,42,106,0.25) 0%, rgba(14,42,106,0.85) 22%, var(--crowd-dark) 40%, #13337a 60%, var(--bg-deep) 100%);
  }

  .headline {
    position: absolute; top: 30px; left: 0; right: 0; text-align: center;
    font-family: "Arvo", "Rockwell", serif; font-weight: 700;
  }
  .headline__main {
    font-size: 116px; line-height: 1.05; color: var(--navy);
    text-shadow: 0 0 4px var(--white), 0 0 8px var(--white), 0 0 2px var(--white);
  }
  .headline__sub {
    margin-top: 0;
    font-size: 54px; line-height: 1.1; color: var(--sky-blue);
    text-shadow: 0 0 3px var(--white), 0 0 6px var(--white);
  }

  .info-panel {
    position: absolute; left: 48px; top: 286px; width: 832px; height: 376px;
    background: var(--panel-fill);
    border: 3px solid var(--panel-edge); border-radius: 14px;
    text-align: center;
    font-family: "Libre Baskerville", "Times New Roman", serif; font-weight: 700;
    color: var(--ink);
  }
  .info-panel__eyebrow { margin-top: 28px; font-size: 29px; }
  .info-panel__title { margin-top: 8px; font-size: 50px; font-weight: 400; color: var(--navy); line-height: 1.1; }
  .info-panel__tagline { margin-top: 10px; font-size: 27px; }
  .info-panel__dates { margin-top: 42px; font-size: 30px; line-height: 1.3; }
  .info-panel__url { margin-top: 10px; font-size: 29px; color: var(--navy); }

  .verses {
    position: absolute; left: 58px; top: 922px; width: 812px;
    font-family: "Tinos", "Times New Roman", serif; font-weight: 700; font-size: 18px; line-height: 1.2;
    color: var(--white);
  }
  .verses p { margin-bottom: 18px; }

  .thanks {
    position: absolute; left: 0; right: 0; top: 1144px; text-align: center;
    font-family: "Tinos", "Times New Roman", serif; font-weight: 700; font-size: 29px;
    color: var(--white);
  }
</style>
</head>
<body>
<main class="poster">
  <div class="artwork" role="img" aria-label="Colourful illustrated globe with city buildings, bridges and clouds on a blue rayed background"></div>
  <div class="crowd" role="img" aria-label="Silhouettes of a worship crowd with raised hands in front of the globe"></div>

  <header class="headline">
    <h1 class="headline__main">The “QKT”s</h1>
    <p class="headline__sub">Bible Verses Banned</p>
  </header>

  <section class="info-panel">
    <p class="info-panel__eyebrow">The Lantern Harbor</p>
    <h2 class="info-panel__title">Summit :</h2>
    <p class="info-panel__tagline">The Deeper Message of God's Relentless Love</p>
    <p class="info-panel__dates">Friday Aug. 5 - Sunday the 7th<br>Denver 2016</p>
    <p class="info-panel__url">www.TheLanternSummit.example</p>
  </section>

  <section class="verses">
    <p>"For God has consigned ALL to disobedience so that He may have mercy on them ALL."<br>(Romans 11:32)</p>
    <p>"He is the atoning sacrifice for our sins, and not only for ours but also for the sins of the whole<br>world." (1 John 2:2)</p>
    <p>"That is why we labor because we trust in the living God who is the savior of all men, especially<br>those who believe." (1 Timothy 4:10)</p>
    <p>"And I, when I am lifted up from the earth, will draw all people to myself."&nbsp; (John 12:32)</p>
  </section>

  <p class="thanks">THANKS!!!</p>
</main>
</body>
</html>
```